Postcard Design

Publicity and Communications
Updates

I had originally uploaded a PPT to show the information on the front and back of the post card. SO I will put the text here. FRONT My LOGO Knight on Horse (Gray) with Gold graphics around it. Key Message: Are your Hunts Tax Deductible? Publicity Package – Show Special: $549 Publicize Your Business – Publicize Your Adventure 1 Press Release (1 Page/300 Words) 1 Interview-Style Feature Article (Up to 800 Words) Price valid through Sept. 15, 2015 Director of Communications is a Hunter - 3 HVL Top Tens – 15 Fletchcraft U.S. Open Finals & World Records - Articles in 1,000’s of TV& Print Media Outlets Publicity from Wall Street to Local News and Company News Letters | Books | Blogs BACK Brell Marrow Media logo 1386 West Calloway Rd. Suite #517 Tucson, AZ 85093 T. (520) 555-0148 M. (321) 555-0193 Janet.Pruvost@BrellMarrow.example www.BrellMarrow.example Low Prices – World Class Results People Who Get Ahead, Promote. Member: CMFO, DLQ, PWVT, GBOE, USA Fletchcraft, TGE, YIPO National Awards: RVMQ, Morwick Pell, Net Outreach Fellowship, Silvery Node Prizes Sample Price Schedule Blogs & Newsletters $2.25/word Press Releases - $2.25/word Periodicals & Interviews - $1.71/word -

Hi - The Back still has problems that are easy to fix The Sample Prices heading is not a bullet point of the AWARDS. It should be equal importance / same design as the AWARDS The prices are XX per word so, please move the "word" text after the price (bring it up from the second bullet to the first) Please refer to the last message. It shows the text in terms of Heading and the way that the text for each type of writing service / price has it's own separate line and price per word Thanks! We're close

Target Market(s)

Hunters, hunting industry, high end safaris, high end birding and fishing, see Tamsel, Dulgrove sites, European traditions; audience is typically 40-70 yr. men and women working in this industry.

Industry/Entity Type

Communications

Colors

Designer to choose colors to be used in the design.

Requirements
Must have
• my logo. Note: I uploaded sketches, but am really open to better graphics and layout. Would like powerful images that are general but high quality reference and an "out of Africa" feel, which I don't think that I have accomplished.
Should not have
• Children and teens

```html
<!DOCTYPE html>
<html lang="en">
<head>
<meta charset="utf-8">
<title>Brell Marrow Media — Publicity Package Postcard</title>
<link rel="stylesheet" href="https://fonts.googleapis.com/css2?family=Open+Sans:wght@400;600;700&display=swap">
<style>
  :root {
    --page: #ffffff;
    --card-bg: #cbc2bb;
    --card-top: #e3ddd8;
    --footer-bg: #e2ddd9;
    --ink: #0d0d0d;
    --gold: #c6843a;
    --brand-ink: #4f4a45;
    --band-dark: #5a4335;
    --band-mid: #8a7668;
    --scene-a: #bdb2aa;
    --scene-b: #d3cbc5;
    --photo-1: #7a6a55;
    --photo-2: #8d8465;
    --photo-3: #6f6a3e;
    --photo-4: #6f8a55;
  }
  * { box-sizing: border-box; margin: 0; padding: 0; }
  html, body {
    width: 1200px; height: 848px; overflow: hidden;
    background: var(--page);
    font-family: "Open Sans", Arial, sans-serif;
  }
  .postcard {
    position: absolute; left: 30px; top: 38px;
    width: 1140px; height: 772px;
    background: var(--card-bg);
    overflow: hidden;
  }
  .postcard__topband {
    position: absolute; left: 0; top: 0; width: 100%; height: 21px;
    background: var(--card-top);
  }
  .scene-backdrop {
    position: absolute; left: 0; top: 191px; width: 100%; height: 479px;
    background:
      radial-gradient(ellipse 220px 260px at 170px 330px, rgba(150,135,120,.35), transparent 70%),
      radial-gradient(ellipse 160px 300px at 960px 330px, rgba(150,135,120,.3), transparent 70%),
      radial-gradient(ellipse 420px 220px at 360px 90px, rgba(150,135,120,.35), transparent 70%),
      linear-gradient(180deg, var(--scene-a), var(--scene-b));
  }
  .photo-strip {
    position: absolute; left: 0; top: 21px; width: 100%; height: 170px;
    display: flex;
  }
  .photo-strip__item { height: 100%; }
  .photo-strip__item--bear  { width: 278px; background: linear-gradient(160deg, #a39683, var(--photo-1)); }
  .photo-strip__item--buck  { width: 306px; background: linear-gradient(160deg, #b0a684, var(--photo-2)); }
  .photo-strip__item--fawn  { width: 257px; background: linear-gradient(160deg, #8f8a58, var(--photo-3)); }
  .photo-strip__item--turkey{ width: 299px; background: linear-gradient(180deg, #d7e2ea 0%, #8aa075 45%, var(--photo-4)); }

  .headline {
    position: absolute; left: 0; top: 212px; width: 100%;
    text-align: center; font-weight: 700; font-size: 62px; color: var(--ink);
    letter-spacing: -0.3px;
  }
  .brand {
    position: absolute; left: 0; top: 408px; width: 100%;
    display: flex; justify-content: center; align-items: center; gap: 12px;
  }
  .brand__dot {
    width: 30px; height: 30px; border-radius: 50%; background: var(--gold);
  }
  .brand__name {
    font-weight: 600; font-size: 24px; color: var(--brand-ink);
  }
  .offer {
    position: absolute; left: 0; top: 490px; width: 100%;
    text-align: center; font-weight: 700; font-size: 36px; color: var(--gold);
  }
  .offer-details {
    position: absolute; left: 0; top: 549px; width: 100%; height: 68px;
    display: flex;
  }
  .offer-details__col {
    text-align: center; font-weight: 600; font-size: 22.5px; line-height: 30px;
    color: var(--ink); display: flex; align-items: center; justify-content: center;
  }
  .offer-details__col--business { width: 420px; padding-left: 30px; }
  .offer-details__col--release  { width: 308px; border-left: 3px solid var(--gold); border-right: 3px solid var(--gold); }
  .offer-details__col--feature  { width: 412px; padding-right: 24px; }
  .validity {
    position: absolute; left: 0; top: 630px; width: 100%;
    text-align: center; font-weight: 600; font-size: 20px; color: var(--ink);
  }
  .hide-band {
    position: absolute; left: 0; top: 670px; width: 100%; height: 30px;
    background: linear-gradient(90deg, var(--band-dark), var(--band-mid) 50%, var(--band-dark));
  }
  .footer {
    position: absolute; left: 0; top: 700px; width: 100%; height: 72px;
    background: var(--footer-bg);
  }
  .footer__line {
    padding-top: 10px; text-align: center; font-size: 20px; color: var(--ink);
  }
</style>
</head>
<body>
  <main class="postcard">
    <div class="postcard__topband"></div>
    <div class="scene-backdrop" role="img" aria-label="Faint African savanna scene with acacia tree, lion and giraffes"></div>
    <div class="photo-strip">
      <div class="photo-strip__item photo-strip__item--bear" role="img" aria-label="Hunter posing with a black bear among rocks"></div>
      <div class="photo-strip__item photo-strip__item--buck" role="img" aria-label="Hunter with rifle and a deer in dry grass"></div>
      <div class="photo-strip__item photo-strip__item--fawn" role="img" aria-label="Hunter with a small antelope in woodland"></div>
      <div class="photo-strip__item photo-strip__item--turkey" role="img" aria-label="Hunter holding a wild turkey in a mountain meadow"></div>
    </div>

    <h1 class="headline">Are your Hunts Tax Deductible?</h1>

    <div class="brand">
      <span class="brand__dot"></span>
      <span class="brand__name">Brell Marrow Media</span>
    </div>

    <p class="offer">Publicity Package - Show Special $549</p>

    <div class="offer-details">
      <div class="offer-details__col offer-details__col--business">Publicize Your Business -<br>Publicize Your Adventure</div>
      <div class="offer-details__col offer-details__col--release">1 Press Release<br>1 Page (300 words)</div>
      <div class="offer-details__col offer-details__col--feature">1 Interview-Style Feature<br>Article (Up to 800 words)</div>
    </div>

    <p class="validity">Price valid through Sept. 15, 2015</p>

    <div class="hide-band" role="img" aria-label="Decorative animal-hide print band"></div>

    <footer class="footer">
      <p class="footer__line">Publicity from Wall Street to Local News and Company Newsletters, Books, Blogs.</p>
    </footer>
  </main>
</body>
</html>
```